Kestrel Photography Business Card

I need a business card designed for a photography business based in Perth, Western Australia called Kestrel Photography.

We specialise in wedding, event photography and portrait photography.

The business card must borrow the style of the attached logo.

The hex codes for the colours in the logo are:
#ED1D85 - Pink
#89C23E - Green
#37282F - Black

The name on the card will be:
Name: Torvane
Phone: 0417395286
Website: www.kestrelphotography.example.au
Facebook: kestrelphotography

I am open and happy to accept creative concepts.

I’d like some space at the back for writing notes and appointment details.

```html
<!DOCTYPE html>
<html lang="en">
<head>
<meta charset="utf-8">
<title>Kestrel Photography – Business Card</title>
<link rel="stylesheet" href="https://fonts.googleapis.com/css2?family=Montserrat:wght@400&display=swap">
<style>
  :root {
    --backdrop: #d3e3d6;
    --pink: #ed1d85;
    --pink-deep: #e3156e;
    --green: #89c23e;
    --ink: #37282f;
    --ink-panel: #483539;
    --paper: #ffffff;
    --mist: #d6d6d6;
    --label: #4a4a4a;
  }
  html, body {
    margin: 0;
    width: 1200px;
    height: 848px;
    overflow: hidden;
    background: var(--backdrop);
    font-family: "Montserrat", Arial, sans-serif;
  }
  .card-front {
    position: absolute;
    left: 220px;
    top: 206px;
    width: 760px;
    height: 436px;
    overflow: hidden;
    background: var(--paper);
  }
  .card-front svg { display: block; }
  .holder-name {
    font-size: 26px;
    letter-spacing: 8px;
    fill: var(--paper);
  }
  .contact-line {
    font-size: 12px;
    letter-spacing: 0.3px;
    fill: var(--paper);
  }
  .brand-name {
    font-size: 15px;
    letter-spacing: 6px;
    fill: var(--label);
  }
</style>
</head>
<body>
  <section class="card-front" aria-label="Kestrel Photography business card, front">
    <svg width="760" height="436" viewBox="0 0 760 436">
      <defs>
        <linearGradient id="pink-sheen" x1="0" y1="0" x2="1" y2="0.4">
          <stop offset="0" stop-color="#f6b4d2"/>
          <stop offset="0.35" stop-color="var(--pink)"/>
          <stop offset="1" stop-color="var(--pink-deep)"/>
        </linearGradient>
        <linearGradient id="mist-fade" x1="1" y1="0" x2="0" y2="0.3">
          <stop offset="0" stop-color="#ffffff"/>
          <stop offset="1" stop-color="var(--mist)"/>
        </linearGradient>
      </defs>

      <rect class="panel-pink" x="0" y="0" width="300" height="300" fill="url(#pink-sheen)"/>
      <polygon class="band-mist" points="300,300 760,170 760,436 300,436" fill="url(#mist-fade)"/>
      <polygon class="panel-ink" points="0,300 560,300 0,436" fill="var(--ink-panel)"/>

      <g class="contact-block">
        <text class="holder-name" x="30" y="104">TORVANE</text>
        <line class="contact-rule" x1="30" y1="124" x2="110" y2="124" stroke="var(--paper)" stroke-width="1.5"/>
        <text class="contact-line" x="30" y="164">0417395286</text>
        <text class="contact-line" x="30" y="190">www.kestrelphotography.example.au</text>
        <text class="contact-line" x="30" y="216">facebook / kestrelphotography</text>
      </g>

      <circle class="brand-dot" cx="530" cy="95" r="56" fill="var(--pink)"/>
      <text class="brand-name" x="530" y="205" text-anchor="middle">KESTREL PHOTOGRAPHY</text>
    </svg>
  </section>
</body>
</html>
```